New Office Poster Designs

Attached you will find 3 poster designs that we found online along with our logos. Please use our logos to reference any type of color or design.
These posters will be hung around our Loan Offices.

INSTRUCTIONS: Please mimic all 3 posters (MINUS THE SMALL WRITING ON THEM THAT IS NOT IN ENGLISH IGNORE THAT)
but use our logos and colors. Also, if you can make them in Spanish as well as English that is a plus. We will also need 1 additional poster with the below wording.

Additional Poster:
Stuck in a Title Loan? Let us pay it off up to $10,000

Target Market(s)

People looking to get a loan and need money

Industry/Entity Type

Loan Industry - Consumer Lending - Fast easy loans

Requirements
Nice to have
• English and Spanish

```html
<!DOCTYPE html>
<html lang="en">
<head>
<meta charset="utf-8">
<title>Stuck in a Title Loan? Poster</title>
<link href="https://fonts.googleapis.com/css2?family=Playfair+Display:wght@700;900&family=Oswald:wght@600&display=swap" rel="stylesheet">
<style>
  :root {
    --backdrop: #e9e9e7;
    --green-deep: #0b3f1c;
    --green-mid: #1e7a34;
    --orange: #d9531e;
    --orange-dark: #b8420f;
    --white: #ffffff;
    --curl-light: #f4f4f4;
    --curl-shade: #9c9c9c;
  }
  * { margin: 0; padding: 0; box-sizing: border-box; }
  html, body {
    width: 1200px;
    height: 3000px;
    overflow: hidden;
    background: var(--backdrop);
  }
  .poster {
    position: absolute;
    left: 50px;
    top: 750px;
    width: 1100px;
    height: 1500px;
    overflow: hidden;
    background: var(--white);
    box-shadow: 0 20px 50px rgba(0,0,0,0.18);
  }
  .poster__photo {
    position: absolute;
    inset: 0;
    background:
      radial-gradient(ellipse 45% 30% at 50% 62%, rgba(120,190,110,0.55), transparent 70%),
      radial-gradient(ellipse 80% 60% at 50% 40%, var(--green-mid), var(--green-deep) 85%);
  }
  .headline {
    position: absolute;
    top: 70px;
    left: 0;
    width: 100%;
    font-family: "Playfair Display", "Times New Roman", serif;
    font-weight: 900;
    color: var(--white);
    line-height: 0.82;
    text-shadow: 0 4px 14px rgba(0,0,0,0.35);
  }
  .headline__big { display: block; font-size: 235px; letter-spacing: -4px; }
  .headline__stuck { padding-left: 170px; }
  .headline__row { display: flex; align-items: flex-end; padding-left: 150px; margin-top: 10px; }
  .headline__small {
    font-size: 78px;
    line-height: 0.9;
    margin-right: 22px;
    margin-bottom: 26px;
    text-align: right;
  }
  .headline__loan { padding-left: 300px; margin-top: 10px; }
  .offer-band {
    position: absolute;
    left: 0;
    top: 1165px;
    width: 800px;
    height: 165px;
    background: linear-gradient(180deg, var(--orange), var(--orange-dark));
    padding: 24px 0 0 60px;
    font-family: "Oswald", "Arial Narrow", sans-serif;
    font-weight: 600;
    font-size: 54px;
    line-height: 1.08;
    color: var(--white);
    letter-spacing: 1px;
  }
  .page-curl {
    position: absolute;
    right: 0;
    bottom: 0;
    width: 420px;
    height: 420px;
  }
  .brand {
    position: absolute;
    right: 40px;
    bottom: 52px;
    display: flex;
    align-items: center;
    gap: 12px;
    font-family: "Oswald", "Arial Narrow", sans-serif;
    font-weight: 600;
    font-size: 40px;
    letter-spacing: 1px;
    color: var(--orange);
  }
  .brand__mark {
    width: 30px;
    height: 30px;
    border-radius: 50%;
    background: var(--orange);
  }
</style>
</head>
<body>
  <main class="poster">
    <div class="poster__photo" role="img" aria-label="Photo of a worried man buried up to his eyes in a pile of dollar bills, tinted green"></div>

    <h1 class="headline">
      <span class="headline__big headline__stuck">Stuck</span>
      <span class="headline__row">
        <span class="headline__small">in<br>a</span>
        <span class="headline__big">Title</span>
      </span>
      <span class="headline__big headline__loan">Loan?</span>
    </h1>

    <p class="offer-band">LET US PAY IT OFF<br>UP TO $10,000</p>

    <svg class="page-curl" viewBox="0 0 420 420" aria-hidden="true">
      <defs>
        <linearGradient id="curlShade" x1="0" y1="0" x2="1" y2="1">
          <stop offset="0" stop-color="#9c9c9c"/>
          <stop offset="0.45" stop-color="#f4f4f4"/>
          <stop offset="0.7" stop-color="#ffffff"/>
          <stop offset="1" stop-color="#c8c8c8"/>
        </linearGradient>
      </defs>
      <path d="M420 40 L420 420 L40 420 Z" fill="#ffffff"/>
      <path d="M420 40 C360 120 300 140 250 150 C230 200 200 260 40 420 L40 420 C150 300 200 230 230 170 C300 160 380 110 420 40 Z" fill="rgba(0,0,0,0.12)"/>
      <path d="M420 40 C380 70 330 90 280 95 C262 130 250 150 250 150 C300 140 360 120 420 40 Z" fill="url(#curlShade)"/>
      <path d="M280 95 C240 110 200 150 190 190 C215 170 235 160 250 150 Z" fill="url(#curlShade)"/>
    </svg>

    <div class="brand">
      <span class="brand__mark"></span>
      <span class="brand__name">CEDARLINE</span>
    </div>
  </main>
</body>
</html>
```